http://www.lanternfieldcollective.org/

would like someone to rebuild this -http://www.lanternfieldcollective.com/ to be more modern and more easily updated

Industry/Entity Type

Non Profit

Coding

Coded - Design and coding required

Colors

Designer to choose colors to be used in the design.

Requirements
Must have
• use of the logo, and a newer design for wordpress to be hosted on Azure and easily updated templates

```html
<!DOCTYPE html>
<html lang="en">
<head>
<meta charset="utf-8">
<title>Lanternfield Collective – Helping the needy Christian families</title>
<link rel="stylesheet" href="https://fonts.googleapis.com/css2?family=Libre+Baskerville:wght@400;700&family=Open+Sans:wght@400;600;700&display=swap">
<style>
:root{
  --plum-deep:#261a36;
  --plum:#3b2852;
  --purple:#6a4a94;
  --gold:#d8b25a;
  --gold-soft:#e8cf8c;
  --cream:#f6efdc;
  --ink:#2e2a33;
  --muted:#6f6a75;
  --line:#ddd8e2;
  --white:#ffffff;
  --canvas:#eeeef1;
}
*{box-sizing:border-box;margin:0;padding:0}
html,body{width:1200px;height:2496px;overflow:hidden}
body{background:var(--canvas);font-family:"Open Sans",Arial,sans-serif;color:var(--ink)}
.page{position:absolute;left:40px;top:0;width:1120px;height:2440px;background:var(--white);overflow:hidden}
.abs{position:absolute}
.serif{font-family:"Libre Baskerville",Georgia,serif}

/* navigation */
.site-nav{left:0;top:0;width:1120px;height:72px;background:var(--plum-deep);display:flex;align-items:center;padding:0 40px}
.brand{display:flex;align-items:center;gap:10px;color:var(--white);font-size:13px;font-weight:600;letter-spacing:.5px}
.brand-dot{width:26px;height:26px;border-radius:50%;background:var(--gold)}
.menu{margin-left:auto;display:flex;gap:26px;align-items:center;font-size:12px;color:#e6e0ee}
.menu .active{color:var(--gold)}
.btn-donate{border:1px solid var(--white);color:var(--white);padding:7px 14px;font-size:11px;font-weight:700;letter-spacing:.5px}

/* hero */
.hero{left:0;top:72px;width:1120px;height:268px;background:linear-gradient(135deg,#2f2142,#3e2b58 55%,#2a1d3b)}
.hero h1{position:absolute;left:0;right:0;top:104px;text-align:center;color:var(--white);font-size:44px;font-weight:700}
.hero .url{position:absolute;left:0;right:0;top:170px;text-align:center;color:#cfc5dc;font-size:12px}

/* intro */
.icon-frame{left:260px;top:340px;width:200px;height:340px;background:linear-gradient(180deg,#8c5a2c,#c79a4a 50%,#6d3b25)}
.portrait{left:340px;top:480px;width:280px;height:260px;background:linear-gradient(180deg,#8a6a55,#3c3434 60%,#1f1c22)}
.intro-text{left:680px;top:600px;width:300px;font-size:12px;line-height:1.7;color:var(--muted)}
.intro-text p{margin-bottom:10px}
.pray{font-size:30px;color:var(--purple);font-weight:600;margin-top:6px}

/* help */
.help-title{left:120px;top:836px;font-size:17px;font-weight:700;color:var(--ink)}
.help-copy{left:120px;top:880px;width:420px;font-size:11.5px;line-height:1.8;color:var(--muted)}
.help-copy p{margin-bottom:14px}
.btn-dark{background:var(--plum-deep);color:var(--white);font-size:11px;font-weight:700;letter-spacing:.6px;padding:12px 20px}
.help-image{left:620px;top:752px;width:500px;height:408px;background:linear-gradient(135deg,#2c2138,#4b3560 60%,#1f1729)}
.quote{left:560px;top:1272px;width:320px;height:148px;background:var(--gold);padding:20px 22px;color:var(--white);font-size:14px;line-height:1.55;font-style:italic}
.quote cite{display:block;margin-top:8px;font-size:11px;font-style:normal;font-weight:700}

/* appeal */
.appeal{left:0;top:1472px;width:1120px;text-align:center;font-size:13px;color:var(--muted)}
.btn-appeal{left:500px;top:1516px;width:120px;height:34px;background:var(--plum-deep);color:var(--white);font-size:11px;display:flex;align-items:center;justify-content:center}

/* contact */
.contact-title{left:0;top:1610px;width:1120px;text-align:center;font-size:34px;font-weight:700;color:var(--ink)}
.contact-mark{left:120px;top:1690px;width:150px;display:flex;flex-direction:column;align-items:center;gap:8px;font-size:12px;font-weight:700;color:var(--plum)}
.contact-mark .disc{width:90px;height:90px;border-radius:50%;background:var(--plum)}
.contact-list{left:120px;top:1820px;font-size:12px;line-height:1.6;color:var(--muted)}
.contact-list li{list-style:none;display:flex;gap:10px;margin-bottom:12px}
.contact-list svg{flex:none;margin-top:2px}
.form{left:580px;top:1680px;width:540px}
.field{border:1px solid var(--line);height:38px;margin-bottom:14px;font-size:11px;color:#a7a2ad;padding:11px 12px}
.field.tall{height:110px}
.btn-send{background:var(--plum);color:var(--white);height:36px;font-size:12px;font-weight:600;display:flex;align-items:center;justify-content:center}

/* story */
.story{left:0;top:2040px;width:1120px;height:360px}
.story h2{position:absolute;left:0;right:0;top:130px;text-align:center;font-size:22px;color:var(--plum);font-weight:700}
.story .copy{position:absolute;left:170px;width:780px;top:180px;text-align:center;font-size:12px;line-height:1.8;color:var(--ink)}
.footer{left:0;top:2400px;width:1120px;height:40px;background:var(--plum-deep);color:#b8afc4;font-size:10px;display:flex;align-items:center;justify-content:space-between;padding:0 40px}
</style>
</head>
<body>
<div class="page">

  <header class="site-nav abs">
    <div class="brand"><span class="brand-dot"></span>Lanternfield Collective</div>
    <nav class="menu">
      <span class="active">Home</span><span>About us</span><span>Projects</span><span>Newsletter &amp; Reports</span><span>Media</span><span>What's New</span><span>Contact Us</span>
      <span class="btn-donate">DONATE NOW</span>
    </nav>
  </header>

  <section class="hero abs" role="img" aria-label="Deep purple hero band with a soft decorative pattern">
    <h1 class="serif">Helping the needy Christian families</h1>
    <div class="url">lanternfieldcollective.org</div>
  </section>

  <div class="icon-frame abs" role="img" aria-label="Painted icon of Christ enthroned in gold and red"></div>
  <div class="portrait abs" role="img" aria-label="Portrait photograph of Father Elias in dark vestments"></div>
  <div class="intro-text abs">
    <p>May God protect and lead in peace our beloved shepherd, Father Elias.</p>
    <p>We pray to our Lord God and Savior Jesus Christ to keep him.</p>
    <div class="pray">Pray for us.</div>
  </div>

  <h2 class="help-title abs">How can you help making our goal accomplished?</h2>
  <div class="help-copy abs">
    <p>Many families in our community face hardship every day. Your gift brings food, shelter, schooling and medical care to those who need it most, and reminds them they are never alone.</p>
    <p>We work with local churches and volunteers who know each family by name. Every donation is used with care, and we share regular reports so you can see the good your support does.</p>
    <p>Join us in prayer, give what you can, or offer your time. Together we can carry hope to homes that have waited far too long for help and kindness.</p>
  </div>
  <div class="btn-dark abs" style="left:120px;top:1120px">LEARN MORE ABOUT US</div>
  <div class="help-image abs" role="img" aria-label="Dark purple photo panel showing a family receiving aid"></div>
  <blockquote class="quote abs">“Assuredly, I say to you, inasmuch as you did it to one of the least of these My brethren, you did it to Me.”<cite>Matthew 25:40</cite></blockquote>

  <p class="appeal abs">We urge you to share with us in this blessed work and to provide a helping hand to the families we serve.</p>
  <div class="btn-appeal abs">Make a donation</div>

  <h2 class="contact-title abs serif">Get in touch</h2>
  <div class="contact-mark abs"><span class="disc"></span>Lanternfield Collective</div>
  <ul class="contact-list abs">
    <li><svg width="14" height="14" viewBox="0 0 24 24"><path d="M12 2C8 2 5 5 5 9c0 5 7 13 7 13s7-8 7-13c0-4-3-7-7-7zm0 9.5A2.5 2.5 0 1 1 12 6.5a2.5 2.5 0 0 1 0 5z" fill="#6a4a94"/></svg><span>PO Box 4417<br>Millbrook Falls, VA 20988</span></li>
    <li><svg width="14" height="14" viewBox="0 0 24 24"><path d="M6.6 10.8a15 15 0 0 0 6.6 6.6l2.2-2.2c.3-.3.7-.4 1-.2 1.1.4 2.3.6 3.6.6.6 0 1 .4 1 1V20c0 .6-.4 1-1 1A17 17 0 0 1 3 4c0-.6.4-1 1-1h3.5c.6 0 1 .4 1 1 0 1.3.2 2.5.6 3.6.1.3 0 .7-.2 1z" fill="#6a4a94"/></svg><span>(555) 014-2290</span></li>
    <li><svg width="14" height="14" viewBox="0 0 24 24"><path d="M3 5h18v14H3z" fill="none" stroke="#6a4a94" stroke-width="2"/><path d="M3 6l9 7 9-7" fill="none" stroke="#6a4a94" stroke-width="2"/></svg><span>hello@lanternfieldcollective.org</span></li>
  </ul>
  <form class="form abs">
    <div class="field">Name</div>
    <div class="field">Email</div>
    <div class="field">Phone</div>
    <div class="field tall">Message</div>
    <div class="btn-send">Send</div>
  </form>

  <section class="story abs">
    <svg class="abs" style="left:0;top:0" width="1120" height="360" viewBox="0 0 1120 360" preserveAspectRatio="none">
      <rect x="0" y="70" width="1120" height="290" fill="#f6efdc"/>
      <path d="M0 40 C200 0 360 90 560 50 S900 10 1120 50 L1120 110 C900 70 740 120 560 95 S200 60 0 100 Z" fill="#d8b25a"/>
      <path d="M0 95 C200 60 360 120 560 100 S900 70 1120 105 L1120 120 C900 95 720 135 560 120 S220 90 0 120 Z" fill="#e8cf8c"/>
    </svg>
    <h2 class="serif">Lanternfield Collective was established April 2004</h2>
    <p class="copy">What we do is rooted in faith and love for our neighbors. From a small circle of friends meeting after church, our work has grown to support hundreds of families each year with food, education and medical care. We believe every act of kindness is an offering, and we thank each of you who walks this road with us in prayer and generosity.</p>
  </section>

  <footer class="footer abs"><span>© 2024 Lanternfield Collective. All rights reserved.</span><span>Privacy · Terms</span></footer>
</div>
</body>
</html>
```